Graphic design for "How It Works" for VelmoraStyles.com*

VelmoraStyles.com website is for selling custom designer outfits for women and girls in all countries, customers can choose existing designs on this website and customize to their measurements. Customers can also provide their own designs and measurements and our expert designers and tailors get the outfit stitched and delivered to the customer.

We wanted to explain how this entire process works in 4 steps in the form of graphic design with little heading and text describing each step.

Step 1: Select Dress
Its time to choose the beauty you want to adorn yourself with. We have a wide collection of premium dresses, colours and accessories. There is something for everyone! All you need to do is pick. If you can’t find what you are looking for then you can share a picture of what you want, we will get it done whatever you want.

Step 2: Customization
Everyone is different; hence we realise the need for customization of the design and size. Here you select exactly how you want your dress to be. From sleeves to cuts, everything will be done as per your wish. Enter your measurements, lo and behold! You’re done. Leave your comments for even more customization.

Step 3: Designer Consultation
We as a user-friendly brand, aspire to provide the best of services to our clients. Our expert lady designers will help you for everything right from selecting of fabric to design of dress to necessary accessories. Our designers are just a call away!

Step 4: Stitch and Deliver
After you have placed your order, we confirm and verify the details. The boutique completes your order, sends it to us and we deliver it to your doorstep. We also have a team of designers in-house to cater to your premium dressing needs.

```html
<!DOCTYPE html>
<html lang="en">
<head>
<meta charset="utf-8">
<title>How It Works – VelmoraStyles.com</title>
<link rel="stylesheet" href="https://fonts.googleapis.com/css2?family=Montserrat:wght@400;600;700;800&family=Open+Sans:wght@400&display=swap">
<style>
  :root {
    --pink: #c94f86;
    --dark: #3d3f44;
    --ink: #34363a;
    --muted: #6b6d72;
    --sheet: #f3f3f4;
    --page: #e6e6e7;
    --white: #ffffff;
  }
  * { margin: 0; padding: 0; box-sizing: border-box; }
  html, body { width: 800px; height: 1200px; overflow: hidden; }
  body { background: var(--page); font-family: "Open Sans", sans-serif; position: relative; }

  .sheet {
    position: absolute; left: 20px; top: 330px;
    width: 760px; height: 540px;
    background: var(--sheet);
    box-shadow: 0 6px 18px rgba(0,0,0,.18);
    overflow: hidden;
  }
  .sheet__bar { position: absolute; left: 0; top: 0; width: 100%; height: 8px; background: var(--dark); }
  .sheet__base { position: absolute; left: 0; bottom: 0; width: 100%; height: 6px; background: var(--dark); }

  .title-tab {
    position: absolute; left: 260px; top: 8px; width: 240px; height: 46px;
    background: var(--pink); border-radius: 0 0 24px 24px;
    color: var(--white); font-family: "Montserrat", sans-serif; font-weight: 700;
    font-size: 25px; display: flex; align-items: center; justify-content: center;
  }

  .diagram { position: absolute; left: 0; top: 0; }

  .step { position: absolute; }
  .step__heading { font-family: "Montserrat", sans-serif; font-weight: 700; font-size: 17px; line-height: 1.15; margin-bottom: 8px; }
  .step__heading--pink { color: var(--pink); }
  .step__heading--dark { color: var(--ink); }
  .step__text { font-size: 9.5px; line-height: 1.5; color: var(--muted); }

  .step--select { left: 28px; top: 215px; width: 160px; }
  .step--custom { left: 182px; top: 78px; width: 176px; }
  .step--consult { left: 420px; top: 70px; width: 180px; }
  .step--deliver { left: 615px; top: 222px; width: 130px; }

  .brand-name {
    position: absolute; left: 280px; top: 470px; width: 200px; text-align: center;
    font-family: "Montserrat", sans-serif; font-weight: 800; font-size: 17px; color: var(--ink);
  }
</style>
</head>
<body>
  <main class="sheet">
    <div class="sheet__bar"></div>
    <h1 class="title-tab">How It Works</h1>

    <svg class="diagram" width="760" height="540" viewBox="0 0 760 540">
      <!-- connecting arc -->
      <path d="M 120 497 A 260 260 0 0 1 640 497" fill="none" stroke="var(--dark)" stroke-width="4"/>
      <!-- leader lines -->
      <g stroke="var(--dark)" stroke-width="1.5">
        <line x1="136" y1="345" x2="136" y2="370"/>
        <line x1="258" y1="205" x2="258" y2="229"/>
        <line x1="502" y1="210" x2="502" y2="229"/>
        <line x1="624" y1="345" x2="624" y2="370"/>
      </g>
      <!-- step markers -->
      <g>
        <circle cx="136" cy="408" r="38" fill="var(--dark)"/>
        <circle cx="258" cy="267" r="38" fill="var(--dark)"/>
        <circle cx="502" cy="267" r="38" fill="var(--dark)"/>
        <circle cx="624" cy="408" r="38" fill="var(--dark)"/>
      </g>
      <g role="img" aria-label="Illustration of browsing a dress collection">
        <circle cx="136" cy="408" r="26" fill="#f1d6e3"/>
      </g>
      <g role="img" aria-label="Illustration of customizing a dress on screen">
        <circle cx="258" cy="267" r="26" fill="#f1d6e3"/>
      </g>
      <g role="img" aria-label="Illustration of a designer consultation call">
        <circle cx="502" cy="267" r="26" fill="#f1d6e3"/>
      </g>
      <g role="img" aria-label="Illustration of stitching and delivery">
        <circle cx="624" cy="408" r="26" fill="#f1d6e3"/>
      </g>
      <!-- central hub -->
      <path d="M 270 497 A 110 110 0 0 1 380 387 L 380 497 Z" fill="var(--pink)"/>
      <path d="M 380 387 A 110 110 0 0 1 490 497 L 380 497 Z" fill="var(--dark)"/>
      <path d="M 302 497 A 78 78 0 0 1 458 497 Z" fill="var(--white)"/>
      <rect x="0" y="497" width="760" height="43" fill="var(--white)"/>
    </svg>

    <p class="brand-name">velmorastyles</p>

    <section class="step step--select">
      <h2 class="step__heading step__heading--pink">Select Dress</h2>
      <p class="step__text">Choose from our wide collection of premium dresses, colours and accessories. Can't find it? Share a picture and we will make it for you.</p>
    </section>
    <section class="step step--custom">
      <h2 class="step__heading step__heading--dark">Customization</h2>
      <p class="step__text">Pick sleeves, cuts and fit exactly as you wish. Enter your measurements and leave comments for even more customization.</p>
    </section>
    <section class="step step--consult">
      <h2 class="step__heading step__heading--pink">Designer<br>Consultation</h2>
      <p class="step__text">Our expert lady designers help you with fabric, design and accessories. They are just a call away.</p>
    </section>
    <section class="step step--deliver">
      <h2 class="step__heading step__heading--dark">Stitch and<br>Deliver</h2>
      <p class="step__text">We verify your order, the boutique stitches it and we deliver it right to your doorstep.</p>
    </section>

    <div class="sheet__base"></div>
  </main>
</body>
</html>
```